Business Card Design for Ferncliff Studios

Design the layout for a two-sided business card incorporating the logo design produced through Pixel Guild by moretundel earlier this year. Design to be created as per specifications for standard size cards produced by Kipt.com. Art work dimensions to be restricted to 3.66" x 2.16"

Front of card to include Ferncliff Studios Logo and name and contact information. Back side to include logo only.

Target Market(s)

Photography clients.

Industry/Entity Type

Business

Contact Information for Business Card

Derek Pahlmann, Photographer
23-815 Otter Bend Drive
Yellowknife, NT X0E 7K2

867-555-3816

derek@ferncliffstudios.example

www.ferncliffstudios.example

Font styles to use
Serif

Requirements
Must have
• Logo, name, contact information, email and website.
• Use colours from original logo design.
Nice to have
• I'm thinking a black background, but I'm open to other ideas.

```html
<!DOCTYPE html>
<html lang="en">
<head>
<meta charset="utf-8">
<title>Ferncliff Studios – Business Card</title>
<link rel="stylesheet" href="https://fonts.googleapis.com/css2?family=Marcellus+SC&family=Open+Sans:wght@300;400&display=swap">
<style>
  :root {
    --backdrop: #929396;
    --card-black: #050607;
    --wave-light: #3b3b3e;
    --wave-dark: #141415;
    --wave-edge: #5a5a5e;
    --gold: #c9a44a;
    --teal: #2aa3b5;
    --ink-light: #e8e8e8;
    --ring: #ffffff;
  }
  html, body {
    margin: 0;
    padding: 0;
    width: 1200px;
    height: 1000px;
    overflow: hidden;
    background: var(--backdrop);
  }
  .canvas { position: relative; width: 1200px; height: 1000px; }
  .card {
    position: absolute;
    left: 289px;
    width: 622px;
    height: 365px;
    box-shadow: 6px 6px 8px rgba(0,0,0,0.35);
    background: var(--card-black);
  }
  .card--front { top: 119px; }
  .card--back { top: 510px; }
  .card svg { display: block; }
  .brand-name { font-family: "Marcellus SC", serif; fill: var(--gold); }
  .brand-sub { font-family: "Marcellus SC", serif; fill: var(--gold); letter-spacing: 5px; }
  .person-first { font-family: "Marcellus SC", serif; fill: var(--gold); }
  .person-last { font-family: "Marcellus SC", serif; fill: var(--teal); }
  .person-role { font-family: "Open Sans", sans-serif; font-weight: 300; fill: var(--ink-light); letter-spacing: 2px; }
  .contact-text { font-family: "Open Sans", sans-serif; font-weight: 400; fill: var(--ink-light); font-size: 12px; }
  .contact-icon { fill: var(--teal); }
  .icon-glyph { fill: none; stroke: #0c1a1c; stroke-width: 1.4; stroke-linecap: round; stroke-linejoin: round; }
  .brand-ring { fill: var(--card-black); stroke: var(--ring); stroke-width: 4; }
</style>
</head>
<body>
<div class="canvas">

  <!-- Front side -->
  <div class="card card--front">
    <svg width="622" height="365" viewBox="0 0 622 365">
      <defs>
        <linearGradient id="waveFill" x1="0" y1="0" x2="0" y2="1">
          <stop offset="0" stop-color="var(--wave-light)"/>
          <stop offset="1" stop-color="var(--wave-dark)"/>
        </linearGradient>
      </defs>
      <path class="wave" d="M0,216 C150,196 300,206 420,276 C500,322 560,352 622,358 L622,365 L0,365 Z" fill="url(#waveFill)"/>
      <path class="wave-edge" d="M0,216 C150,196 300,206 420,276 C500,322 560,352 622,358" fill="none" stroke="var(--wave-edge)" stroke-width="1"/>

      <circle class="brand-ring" cx="76" cy="73" r="36"/>
      <text class="brand-name" x="121" y="79" font-size="30">Ferncliff</text>
      <text class="brand-sub" x="168" y="96" font-size="12">STUDIOS</text>

      <text x="52" y="159" font-size="34"><tspan class="person-first">Derek </tspan><tspan class="person-last">Pahlmann</tspan></text>
      <text class="person-role" x="53" y="183" font-size="18">Photographer</text>

      <g class="contact-list">
        <circle class="contact-icon" cx="59" cy="245" r="8"/>
        <path class="icon-glyph" d="M55,242 q1,5 6,7 l1.5,-1.5 l-2,-2 l-1,1 q-2,-1 -3,-3 l1,-1 l-2,-2 z"/>
        <text class="contact-text" x="74" y="249">867-555-3816</text>

        <circle class="contact-icon" cx="59" cy="265" r="8"/>
        <rect class="icon-glyph" x="54.5" y="261.5" width="9" height="7"/>
        <path class="icon-glyph" d="M54.5,261.5 L59,265.5 L63.5,261.5"/>
        <text class="contact-text" x="74" y="269">derek@ferncliffstudios.example</text>

        <circle class="contact-icon" cx="59" cy="285" r="8"/>
        <circle class="icon-glyph" cx="59" cy="285" r="4.5"/>
        <path class="icon-glyph" d="M54.5,285 H63.5 M59,280.5 V289.5"/>
        <text class="contact-text" x="74" y="289">www.ferncliffstudios.example</text>

        <circle class="contact-icon" cx="59" cy="306" r="8"/>
        <path class="icon-glyph" d="M59,312 C56,308 55,306 55,304 A4,4 0 0 1 63,304 C63,306 62,308 59,312 Z"/>
        <text class="contact-text" x="75" y="312">23-815 Otter Bend Drive</text>
        <text class="contact-text" x="75" y="325">Yellowknife, NT X0E 7K2</text>
      </g>
    </svg>
  </div>

  <!-- Back side -->
  <div class="card card--back">
    <svg width="622" height="365" viewBox="0 0 622 365">
      <defs>
        <linearGradient id="waveTop" x1="0" y1="0" x2="0" y2="1">
          <stop offset="0" stop-color="var(--wave-dark)"/>
          <stop offset="1" stop-color="var(--wave-light)"/>
        </linearGradient>
        <linearGradient id="waveBottom" x1="0" y1="0" x2="0" y2="1">
          <stop offset="0" stop-color="var(--wave-light)"/>
          <stop offset="1" stop-color="var(--wave-dark)"/>
        </linearGradient>
      </defs>
      <path class="wave" d="M130,0 C250,40 330,108 470,122 C540,128 600,118 622,114 L622,0 Z" fill="url(#waveTop)"/>
      <path class="wave-edge" d="M130,0 C250,40 330,108 470,122 C540,128 600,118 622,114" fill="none" stroke="var(--wave-edge)" stroke-width="1"/>

      <path class="wave" d="M0,238 C150,224 300,226 420,280 C500,318 560,355 610,365 L0,365 Z" fill="url(#waveBottom)"/>
      <path class="wave-edge" d="M0,238 C150,224 300,226 420,280 C500,318 560,355 610,365" fill="none" stroke="var(--wave-edge)" stroke-width="1"/>

      <circle class="brand-ring" cx="209" cy="177" r="36"/>
      <text class="brand-name" x="254" y="183" font-size="30">Ferncliff</text>
      <text class="brand-sub" x="301" y="200" font-size="12">STUDIOS</text>
    </svg>
  </div>

</div>
</body>
</html>
```